Journal indexing service aimed at teachers

We are keen to redesign the appearance and functionality of lessonkite.co.nz, a site aimed at teachers.
Lessonkite provides teachers with a the ability to search for teaching resources in a printed journal series.

Clickable wireframes of the intended functionality can be seen at:
http://lessonkite.vandorpress.co.nz/wireframes
user: administrator
password: lessonkite

These wireframes are also attached here as a zip file (you'll need an Internet connection to see the images when loading them in a browser).

The redesigned site needs to be attractive and easy for users to use, and should be friendly and not too business / corporate-like.

The high majority of users will be only interested in the search functionality (which is why it is so prominent throughout the site).

We don't particularly want to continue using the current pink colouring and logo of the existing site, so please ignore these.

It also needs to be able to be responsive such that it can be used on desktop computers and tablets (though not phones).

Any design submissions should be based on treatments of
* The home page:
http://lessonkite.vandorpress.co.nz/wireframes/#/page=5AE161CA82577B2894710D933DA68252
* The search results page:
http://lessonkite.vandorpress.co.nz/wireframes/#/page=7C6A2B8FF40D5075FE250E12A37B03C5
http://lessonkite.vandorpress.co.nz/wireframes/#/page=EF9491C1CB205D41D09A0E59219E4870

We expect to have to support browsers back to IE8, though we can use polyfills to use modern web conventions in these older browsers.

Reason: Deadline for the designs of the Journal indexing service has been extended by another 7 days -- please let me know if anyone has any questions.

Target Market(s)

Primary school teachers

Industry/Entity Type

Business

Colors

Designer to choose colors to be used in the design.

Requirements
Must have
• Must be friendly and inviting
Should not have
• Should not be too business-like

```html
<!DOCTYPE html>
<html lang="en">
<head>
<meta charset="utf-8">
<title>Lessonkite – Online Catalogue of the Harbour Reader</title>
<link rel="stylesheet" href="https://fonts.googleapis.com/css2?family=Roboto+Condensed:wght@400;700&family=Arimo:wght@400;700&display=swap">
<style>
:root{
  --red:#c1353a;
  --red-dark:#a8282d;
  --ink:#333333;
  --body:#555555;
  --muted:#777777;
  --rule:#d6d6d6;
  --hero-top:#f4f4f4;
  --hero-bottom:#cfcfcf;
  --white:#ffffff;
}
*{box-sizing:border-box;margin:0;padding:0}
html,body{width:867px;height:1200px;overflow:hidden;background:var(--white)}
body{position:relative;font-family:"Arimo",Arial,sans-serif;color:var(--body)}
.abs{position:absolute}
.cond{font-family:"Roboto Condensed","Arial Narrow",sans-serif}

/* header */
.site-header{left:0;top:0;width:867px;height:66px;background:#fafafa}
.brand{left:124px;top:10px}
.brand-name{font-family:"Roboto Condensed",sans-serif;font-weight:400;font-size:24px;color:var(--red);line-height:24px;letter-spacing:.5px}
.brand-tag{font-size:7px;color:#34507a;line-height:9px;margin-top:3px;padding-left:10px}
.call{right:126px;top:20px;display:flex;align-items:center;gap:8px;font-size:10.5px;color:var(--ink)}

/* nav */
.main-nav{left:0;top:66px;width:867px;height:28px;background:var(--red)}
.main-nav a{position:absolute;top:0;height:28px;line-height:28px;font-size:8px;color:var(--white);text-decoration:none;text-align:center}
.main-nav a.active{background:var(--red-dark)}

/* hero */
.hero{left:0;top:94px;width:867px;height:306px;background:linear-gradient(var(--hero-top),#e6e6e6 60%,var(--hero-bottom))}
.hero-base{left:0;top:375px;width:867px;height:24px;background:linear-gradient(#e9e9e9,#c9c9c9);border-top:2px solid #fff;border-bottom:2px solid #9a9a9a}
.slide-side{top:146px;height:198px;width:138px;background:linear-gradient(#c6b277,#8f85a0 45%,#6e6340)}
.slide-right{background:linear-gradient(#3b4a45,#4f7688 40%,#2d3a3d)}
.tablet{left:302px;top:142px;width:268px;height:206px;border-radius:12px;background:#1c1c1c;padding:16px 24px}
.tablet-screen{width:100%;height:100%;background:linear-gradient(#cdb46a 0 30%,#c8c8b8 30%,#7b8d86 80%,#3f5b5e)}
.arrow-btn{top:224px;width:30px;height:30px;background:var(--red);display:flex;align-items:center;justify-content:center}

/* welcome */
.welcome{left:124px;top:434px;width:244px;text-align:right}
.welcome h1{font-family:"Roboto Condensed",sans-serif;font-weight:400;font-size:16px;color:var(--red);line-height:20px}
.welcome h2{font-family:"Roboto Condensed",sans-serif;font-weight:400;font-size:14.5px;color:var(--ink);line-height:20px;margin-top:3px;text-align:left}
.btn{display:inline-block;background:var(--red);color:var(--white);font-family:"Roboto Condensed",sans-serif;font-weight:700;text-decoration:none;text-align:center}
.welcome-btns{left:167px;top:493px;display:flex;gap:14px}
.welcome-btns .btn{height:28px;line-height:28px;font-size:11px}
.welcome-note{left:150px;top:533px;width:219px;text-align:right;font-size:9px;line-height:16px;color:var(--ink)}
.divider{left:406px;top:428px;width:12px;height:136px}
.intro{left:444px;top:435px;width:282px;font-size:7.2px;line-height:15px;color:var(--body)}
.intro p+p{margin-top:15px}
.section-rule{left:134px;top:591px;width:600px;height:3px;background:radial-gradient(ellipse at center,#cfcfcf,rgba(255,255,255,0) 70%)}

/* news */
.news-title{left:124px;top:614px;font-family:"Roboto Condensed",sans-serif;font-size:16px;color:var(--red)}
.news-card{top:647px;width:190px}
.news-img{width:190px;height:114px}
.news-card h3{font-family:"Roboto Condensed",sans-serif;font-weight:400;font-size:8.5px;color:var(--ink);margin-top:12px}
.news-date{font-size:7.2px;font-style:italic;color:var(--red);margin-top:6px;padding-left:1px}
.news-card hr{border:0;border-top:1px solid var(--rule);margin-top:8px}
.news-card p{font-size:7.2px;line-height:15px;margin-top:9px}
.read-more{height:16px;line-height:16px;width:61px;font-size:7px;margin-top:10px;border-radius:2px}
.view-more{left:366px;top:929px;width:135px;height:28px;line-height:28px;font-size:11px;border-radius:2px}

/* footer */
.site-footer{left:0;top:988px;width:867px;height:212px;background:linear-gradient(#d9d9d9,#f4f4f4 25%,#ffffff 60%)}
.foot-head{font-family:"Roboto Condensed",sans-serif;font-size:10.5px;color:var(--red)}
.foot-links{left:142px;top:1037px;list-style:none;font-size:8px;color:var(--ink)}
.foot-links li{height:21.6px}
.contact-line{font-size:8px;color:var(--ink);display:flex;align-items:center;gap:6px}
.share{left:285px;top:1109px;display:flex;align-items:center;gap:6px}
.share span{font-family:"Roboto Condensed",sans-serif;font-size:8px;color:var(--red)}
.share i{display:block;width:20px;height:20px;border-radius:50%;background:#8f8f8f}
.badge{top:1144px;width:50px;height:14px;border-radius:2px}
.field{left:481px;width:165px;height:19px;border:1px solid #bdbdbd;background:var(--white);font-size:7.5px;color:var(--ink);line-height:17px;padding-left:8px}
.signup{left:531px;top:1094px;width:116px;height:29px;line-height:29px;font-size:11px;border-radius:2px}
.copyright{left:476px;top:1149px;font-size:8px;color:var(--ink)}
</style>
</head>
<body>

<header class="abs site-header">
  <div class="abs brand">
    <div class="brand-name">Lessonkite</div>
    <div class="brand-tag">Online Catalogue of the Harbour Reader<br>and other resources</div>
  </div>
  <div class="abs call">
    <svg width="26" height="26" viewBox="0 0 26 26" aria-hidden="true"><circle cx="13" cy="13" r="12" fill="none" stroke="#222" stroke-width="1.6"/><path d="M9 7c-1 1-1.6 2-1 3.6 1 3 3.6 6 6.6 7.4 1.5.6 2.6 0 3.4-1l-2.2-2.2-1.6 1c-1.6-.8-3-2.2-3.6-3.8l1-1.6z" fill="#222"/></svg>
    <span>Call Us : 021 555 0142</span>
  </div>
</header>

<nav class="abs main-nav">
  <a class="active" style="left:124px;width:80px">HOME</a>
  <a style="left:220px;width:40px">NEWS</a>
  <a style="left:298px;width:60px">RESOURCES</a>
  <a style="left:398px;width:40px">ABOUT</a>
  <a style="left:474px;width:40px">HELP</a>
  <a style="left:548px;width:68px">CONTACT US</a>
</nav>

<section class="abs hero">
</section>
<div class="abs slide-side" style="left:164px" role="img" aria-label="Journal cover with a sunset over the sea"></div>
<div class="abs slide-side slide-right" style="left:570px" role="img" aria-label="Journal cover with a breaking ocean wave"></div>
<div class="abs tablet"><div class="tablet-screen" role="img" aria-label="Tablet showing a journal cover with a calm beach scene"></div></div>
<div class="abs hero-base"></div>
<a class="abs arrow-btn" style="left:118px" aria-label="Previous"><svg width="10" height="14" viewBox="0 0 10 14"><path d="M8 1 2 7l6 6" fill="none" stroke="#fff" stroke-width="1.6"/></svg></a>
<a class="abs arrow-btn" style="left:718px" aria-label="Next"><svg width="10" height="14" viewBox="0 0 10 14"><path d="M2 1l6 6-6 6" fill="none" stroke="#fff" stroke-width="1.6"/></svg></a>

<section>
  <div class="abs welcome">
    <h1>WELCOME TO LESSONKITE!</h1>
    <h2>ONLINE CATALOGUE OF THE HARBOUR READER</h2>
  </div>
  <div class="abs welcome-btns">
    <a class="btn" style="width:85px">LOGIN &raquo;</a>
    <a class="btn" style="width:103px">SUBSCRIBE &raquo;</a>
  </div>
  <p class="abs welcome-note">Subscribe now and get your first month of access to Lessonkite free!</p>
  <svg class="abs divider" viewBox="0 0 12 136" aria-hidden="true"><path d="M2 0v60l6 6-6 6v64" fill="none" stroke="#dcdcdc" stroke-width="2"/></svg>
  <div class="abs intro">
    <p>Access the best of New Zealand's school resources in the form of more than twenty years of the Harbour Reader Series.</p>
    <p>Lessonkite lets you easily search through the Harbour Reader articles to help you find the right resources to aid your teaching.</p>
    <p>We also provide a growing collection of news articles and curriculum resources, and aim to become your one stop shop for New Zealand edcuation needs.</p>
  </div>
  <div class="abs section-rule"></div>
</section>

<section>
  <h2 class="abs news-title">NEWS</h2>
  <article class="abs news-card" style="left:124px">
    <div class="news-img" style="background:linear-gradient(#dfe8e4,#4e8f98 45%,#1e5a74)" role="img" aria-label="Surfer riding inside a curling wave"></div>
    <h3>GROWING COLLECTION OF NEWS</h3>
    <div class="news-date">Friday March 23rd, 2014</div>
    <hr>
    <p>Many desktop publishing packages and web page editors now use Lorem Ipsum as their default model text, and a search for 'lorem ipsum' will uncover many web sites still in their infancy.</p>
    <a class="btn read-more">READ MORE</a>
  </article>
  <article class="abs news-card" style="left:339px">
    <div class="news-img" style="background:linear-gradient(#3c3a38,#b8b2a6 40%,#4a4845 70%,#2a2826)" role="img" aria-label="Silhouette holding a surfboard on the beach at sunset"></div>
    <h3>GROWING COLLECTION OF NEWS</h3>
    <div class="news-date">Friday March 23rd, 2014</div>
    <hr>
    <p>Many desktop publishing packages and web page editors now use Lorem Ipsum as their default model text, and a search for 'lorem ipsum' will uncover many web sites still in their infancy.</p>
    <a class="btn read-more">READ MORE</a>
  </article>
  <article class="abs news-card" style="left:553px">
    <div class="news-img" style="background:linear-gradient(#d9795a,#e7946e 60%,#2f4e6a)" role="img" aria-label="Surfer silhouette jumping a wave against an orange sky"></div>
    <h3>GROWING COLLECTION OF NEWS</h3>
    <div class="news-date">Friday March 23rd, 2014</div>
    <hr>
    <p>Many desktop publishing packages and web page editors now use Lorem Ipsum as their default model text, and a search for 'lorem ipsum' will uncover many web sites still in their infancy.</p>
    <a class="btn read-more">READ MORE</a>
  </article>
  <a class="abs btn view-more">VIEW MORE NEWS &raquo;</a>
</section>

<footer class="abs site-footer"></footer>
<h4 class="abs foot-head" style="left:143px;top:1016px">WELCOME</h4>
<ul class="abs foot-links">
  <li>Home</li><li>News</li><li>Resources</li><li>About</li><li>Help</li><li>Contact Us</li>
</ul>
<h4 class="abs foot-head" style="left:285px;top:1016px">CONTACT US</h4>
<div class="abs contact-line" style="left:284px;top:1038px">Lessonkite Customer Services</div>
<div class="abs contact-line" style="left:285px;top:1056px">
  <svg width="10" height="15" viewBox="0 0 10 15" aria-hidden="true"><rect x="1" y="1" width="8" height="13" rx="1" fill="none" stroke="#555" stroke-width="1.2"/><rect x="2.5" y="3" width="5" height="8" fill="#555"/></svg>
  Phone: 021 555 0142</div>
<div class="abs contact-line" style="left:285px;top:1082px">
  <svg width="10" height="8" viewBox="0 0 10 8" aria-hidden="true"><rect width="10" height="8" fill="#888"/><path d="M0 0l5 4 5-4" fill="none" stroke="#fff" stroke-width="1"/></svg>
  Email: info@lessonkite.co.nz</div>
<div class="abs share"><span>SHARE :</span><i></i><i></i><i></i><i></i></div>
<div class="abs badge" style="left:285px;background:#3b5a9a"></div>
<div class="abs badge" style="left:341px;background:#5aaad6"></div>
<h4 class="abs foot-head" style="left:483px;top:1016px">GET OUR NEWSLETTER</h4>
<div class="abs field" style="top:1039px">Your Name :</div>
<div class="abs field" style="top:1066px">Your Email :</div>
<a class="abs btn signup">SIGN UP NOW &raquo;</a>
<p class="abs copyright">Copyright © 2014 Lessonkite. All rights reserved.</p>

</body>
</html>
```